Flyer Tally Your Ledger Free

Hi
Can you please design me a DL Flyer for: Tally Your Ledger Free
Info:
Starting a new Business ?
Want to save on bookkeeping fees for your existing business?

You can now save 1000's off bookkeeping fees by Doing it Yourself.

Using our Bookkeeper software you simply key in the information as you go.

We offer one on one training, backup and support.
We can assist you with BAS Preparation and Payrol Advice.

Add Modules as required:
Point of Sale Module
Jobs Management Module
Website Intergration Module

Fee set up assistance and training.

Lets get the ball rolling: 1300 642 815
www.tylfr.com.au
admin@tylfr.com.au (use the logo thing you made)

Target Market(s)

Small Business

Colors
ec1f27
f04a50
f59296
fcdcdc
ffffff

Requirements
Nice to have
• image/s related to bookkeeping

```html
<!DOCTYPE html>
<html lang="en">
<head>
<meta charset="utf-8">
<title>Tally Your Ledger Free – Flyer</title>
<link href="https://fonts.googleapis.com/css2?family=Bebas+Neue&family=Kaushan+Script&family=Source+Sans+3:wght@300;400;600;700&display=swap" rel="stylesheet">
<style>
  :root {
    --brand-red: #ec1f27;
    --brand-red-soft: #f04a50;
    --brand-pink: #f59296;
    --brand-blush: #fcdcdc;
    --white: #ffffff;
    --panel-dark: #3d3e40;
    --ink: #111111;
    --text-grey: #3a3a3a;
    --photo-wall: #5a4a3e;
    --photo-navy: #22304a;
    --photo-shadow: #1d222b;
    --photo-grey: #8d9098;
    --photo-denim: #a9c3dc;
  }
  * { margin: 0; padding: 0; box-sizing: border-box; }
  html, body { width: 1200px; height: 2546px; overflow: hidden; background: var(--white); }
  .flyer { position: relative; width: 1200px; height: 2546px; background: var(--white); overflow: hidden; font-family: "Source Sans 3", Arial, sans-serif; }

  .hero { position: absolute; left: 0; top: 0; width: 1200px; height: 1100px; }

  .modules {
    position: absolute; left: 97px; top: 1137px; width: 1006px; height: 448px;
    background: var(--panel-dark); border-radius: 46px; color: var(--white);
  }
  .modules-title {
    font-family: "Bebas Neue", Impact, sans-serif; font-size: 90px; line-height: 1;
    text-align: center; margin-top: 30px; letter-spacing: 0.3px;
  }
  .module-list { list-style: none; margin: 22px 0 0 94px; }
  .module-list li {
    position: relative; padding-left: 74px; font-size: 57px; font-weight: 300;
    line-height: 97px; height: 97px; white-space: nowrap;
  }
  .module-list li::before {
    content: ""; position: absolute; left: 0; top: 31px; width: 36px; height: 36px;
    border-radius: 50%; background: var(--white);
  }

  .offer-band {
    position: absolute; left: 0; top: 1651px; width: 1200px; height: 152px;
    background: var(--brand-red); color: var(--white);
    font-family: "Bebas Neue", Impact, sans-serif; font-size: 97px; line-height: 158px;
    text-align: center; white-space: nowrap;
  }

  .call-to-action {
    position: absolute; left: 48px; top: 1980px;
    font-family: "Kaushan Script", cursive; font-size: 112px; line-height: 1; color: var(--ink);
    transform: rotate(-13.5deg); transform-origin: left center; white-space: nowrap;
    text-shadow: 6px 6px 6px rgba(0,0,0,0.35);
  }

  .contact { position: absolute; left: 0; width: 1200px; text-align: center; line-height: 1; white-space: nowrap; }
  .contact-phone { top: 2077px; font-size: 96px; font-weight: 700; color: var(--brand-red); letter-spacing: 1px; }
  .contact-web, .contact-email { font-size: 62px; color: var(--text-grey); letter-spacing: 16px; font-weight: 400; }
  .contact-web { top: 2190px; }
  .contact-email { top: 2273px; }

  .brand { position: absolute; left: 0; top: 2398px; width: 1200px; display: flex; align-items: center; justify-content: center; gap: 22px; }
  .brand-dot { width: 60px; height: 60px; border-radius: 50%; background: var(--brand-red); }
  .brand-name { font-size: 66px; font-weight: 600; color: var(--brand-red); line-height: 1; }
</style>
</head>
<body>
<main class="flyer">
  <svg class="hero" viewBox="0 0 1200 1100" xmlns="http://www.w3.org/2000/svg">
    <defs>
      <linearGradient id="heroTone" x1="0" y1="0" x2="0.35" y2="1">
        <stop offset="0" stop-color="var(--photo-wall)"/>
        <stop offset="0.3" stop-color="var(--photo-shadow)"/>
        <stop offset="0.55" stop-color="var(--photo-navy)"/>
        <stop offset="0.78" stop-color="var(--photo-grey)"/>
        <stop offset="1" stop-color="var(--photo-denim)"/>
      </linearGradient>
    </defs>
    <path class="hero-swoosh" d="M0 0 H1200 V903 Q600 1303 0 862 Z" fill="var(--brand-red)"/>
    <path role="img" aria-label="Photo of a young man in glasses and a navy t-shirt sitting outdoors, typing on a laptop on his knee"
          d="M0 0 H1200 V905 Q600 1272 0 750 Z" fill="url(#heroTone)"/>
  </svg>

  <section class="modules">
    <h2 class="modules-title">Add Modules as Required</h2>
    <ul class="module-list">
      <li>Point of Sale Module</li>
      <li>Jobs Management Module</li>
      <li>Website Intergration Module</li>
    </ul>
  </section>

  <div class="offer-band">Fee Set Up Assistance and Training</div>

  <p class="call-to-action">Let’s get the ball rolling</p>

  <p class="contact contact-phone">1300 642 815</p>
  <p class="contact contact-web">www.tylfr.com.au</p>
  <p class="contact contact-email">admin@tylfr.com.au</p>

  <div class="brand">
    <span class="brand-dot"></span>
    <span class="brand-name">Tally Your Ledger Free</span>
  </div>
</main>
</body>
</html>
```